I would like to modify/update my 2 step login screen

I want a more modern looking login page for our document imaging application. I need to keep all of the same elements and buttons that currently exist. The first 2 screens are the login. The 3rd is a screenshot of the actual application home page.

```html
<!DOCTYPE html>
<html lang="en">
<head>
<meta charset="utf-8">
<title>Northfield Systems – Login Screens</title>
<link href="https://fonts.googleapis.com/css2?family=Inter:wght@400;500;600&display=swap" rel="stylesheet">
<style>
  :root {
    --board: #1b1b1b;
    --screen: #f6f7fb;
    --card: #ffffff;
    --ink: #1c2230;
    --muted: #7b8494;
    --field: #eef0f5;
    --line: #e4e7ee;
    --green: #22b02a;
    --green-ink: #ffffff;
  }
  * { box-sizing: border-box; margin: 0; padding: 0; }
  html, body { width: 1200px; height: 863px; overflow: hidden; }
  body {
    background: var(--board);
    font-family: "Inter", Arial, sans-serif;
    color: var(--ink);
    position: relative;
  }
  .screen {
    position: absolute;
    width: 500px;
    height: 344px;
    background: var(--screen);
  }
  .screen--top-left { left: 50px; top: 36px; }
  .screen--top-right { left: 653px; top: 36px; }
  .screen--bottom-left { left: 50px; top: 458px; }
  .screen--bottom-right { left: 653px; top: 458px; }

  .brand {
    position: absolute;
    left: 0; right: 0; top: 52px;
    display: flex; align-items: center; justify-content: center; gap: 5px;
    font-size: 9px; line-height: 12px; font-weight: 600; letter-spacing: 0.02em; color: var(--ink);
  }
  .brand__square { width: 9px; height: 9px; background: var(--ink); }

  .card {
    position: absolute;
    left: 180px; width: 140px; top: 92px;
    background: var(--card);
    border-radius: 3px;
    box-shadow: 0 1px 4px rgba(20, 30, 50, 0.08);
  }
  .card--sso { height: 156px; }
  .card--classic { height: 113px; }
  .card__title {
    position: absolute; left: 0; right: 0; top: 14px;
    text-align: center; font-size: 7.5px; line-height: 10px; font-weight: 500;
  }
  .field, .btn, .provider {
    position: absolute; left: 12px; width: 116px; height: 15px;
    border-radius: 1.5px; font-size: 4.2px; line-height: 6px;
    display: flex; align-items: center;
  }
  .field { background: var(--field); color: var(--muted); padding-left: 4px; }
  .field--focused {
    background: var(--card); border: 0.8px solid #5c6474; color: var(--ink);
  }
  .field__label {
    position: absolute; top: -2.5px; left: 4px;
    font-size: 2.8px; line-height: 4px; background: var(--card); padding: 0 1px; color: var(--muted);
  }
  .field__caret { width: 0.6px; height: 5px; background: var(--ink); }
  .btn {
    background: var(--green); color: var(--green-ink);
    justify-content: center; font-weight: 600;
  }
  .divider {
    position: absolute; left: 12px; width: 116px; top: 79px;
    height: 0.6px; background: var(--line);
  }
  .provider {
    background: var(--card); border: 0.6px solid var(--line);
    justify-content: center; color: var(--ink);
  }
  .provider__mark {
    position: absolute; left: 7px; width: 4.5px; height: 4.5px;
  }
  .provider__mark--circle { border-radius: 50%; border: 1px solid #4a85f0; }
  .provider__mark--square { background: #f2a33a; }
  .provider__mark--dot { border-radius: 50%; background: var(--ink); }
  .forgot {
    position: absolute; right: 12px; top: 96px;
    font-size: 4px; line-height: 6px; font-weight: 500; white-space: nowrap; color: var(--ink);
  }
  .legal {
    position: absolute; left: 0; right: 0; top: 293px;
    text-align: center; font-size: 3.6px; line-height: 5px; color: var(--muted);
  }
  .legal__copyright { margin-top: 7px; }
</style>
</head>
<body>

  <section class="screen screen--top-left" aria-label="Login step one">
    <div class="brand"><span class="brand__square"></span>NORTHFIELD SYSTEMS</div>
    <div class="card card--sso">
      <h1 class="card__title">Log in to NFSS</h1>
      <div class="field" style="top:33px">Enter Database</div>
      <div class="btn" style="top:53px">Log in with my NFView</div>
      <div class="divider"></div>
      <div class="provider" style="top:90px"><span class="provider__mark provider__mark--circle"></span>Log in with Orbitly</div>
      <div class="provider" style="top:110px"><span class="provider__mark provider__mark--square"></span>Log in with Tessellate</div>
      <div class="provider" style="top:129px"><span class="provider__mark provider__mark--dot"></span>Log in with SoloSign</div>
    </div>
    <footer class="legal">
      <p>All activity on this site is recorded.</p>
      <p>Your IP Address is being saved as '203.0.113.184'.</p>
      <p class="legal__copyright">Copyright © 2007-2024 NF Northfield Systems</p>
    </footer>
  </section>

  <section class="screen screen--top-right" aria-label="Classic login step">
    <div class="brand"><span class="brand__square"></span>NORTHFIELD SYSTEMS</div>
    <div class="card card--classic">
      <h1 class="card__title">Classic Log in</h1>
      <div class="field" style="top:35px">Username</div>
      <div class="field" style="top:55px">Password</div>
      <div class="btn" style="top:74px">Log in to NFSSDEMO23</div>
      <span class="forgot">Forgot your password?</span>
    </div>
    <footer class="legal">
      <p>All activity on this site is recorded.</p>
      <p>Your IP Address is being saved as '203.0.113.184'.</p>
      <p class="legal__copyright">Copyright © 2007-2024 NF Northfield Systems</p>
    </footer>
  </section>

  <section class="screen screen--bottom-left" aria-label="Login step one">
    <div class="brand"><span class="brand__square"></span>NORTHFIELD SYSTEMS</div>
    <div class="card card--sso">
      <h1 class="card__title">Log in to NFSS</h1>
      <div class="field" style="top:33px">Enter Database</div>
      <div class="btn" style="top:53px">Log in with my NFView</div>
      <div class="divider"></div>
      <div class="provider" style="top:90px"><span class="provider__mark provider__mark--circle"></span>Log in with Orbitly</div>
      <div class="provider" style="top:110px"><span class="provider__mark provider__mark--square"></span>Log in with Tessellate</div>
      <div class="provider" style="top:129px"><span class="provider__mark provider__mark--dot"></span>Log in with SoloSign</div>
    </div>
    <footer class="legal">
      <p>All activity on this site is recorded.</p>
      <p>Your IP Address is being saved as '203.0.113.184'.</p>
      <p class="legal__copyright">Copyright © 2007-2024 NF Northfield Systems</p>
    </footer>
  </section>

  <section class="screen screen--bottom-right" aria-label="Login step one, database field focused">
    <div class="brand"><span class="brand__square"></span>NORTHFIELD SYSTEMS</div>
    <div class="card card--sso">
      <h1 class="card__title">Log in to NFSS</h1>
      <div class="field field--focused" style="top:33px"><span class="field__label">Database</span><span class="field__caret"></span></div>
      <div class="btn" style="top:53px">Log in with my NFView</div>
      <div class="divider"></div>
      <div class="provider" style="top:90px"><span class="provider__mark provider__mark--circle"></span>Log in with Orbitly</div>
      <div class="provider" style="top:110px"><span class="provider__mark provider__mark--square"></span>Log in with Tessellate</div>
      <div class="provider" style="top:129px"><span class="provider__mark provider__mark--dot"></span>Log in with SoloSign</div>
    </div>
    <footer class="legal">
      <p>All activity on this site is recorded.</p>
      <p>Your IP Address is being saved as '203.0.113.184'.</p>
      <p class="legal__copyright">Copyright © 2007-2024 NF Northfield Systems</p>
    </footer>
  </section>

</body>
</html>
```